Harvest Quorum Lumera LLC

I am starting/launching my IT Consulting company in the Washington DC area. I just finished the logo design with ArtHive with the color palette in the attach. The mission and vision of the company is to help clients (mainly Federal Govt) "lumera" their business digital and business transformation journey . The name is intentional to incorporate my HQ initials. I would like to have a PPT template for the company with a few different pages so it covers a text, table grids. I found a Velotrix PPT Sales Pitch template with new/modern design that Im attaching here as an example. I would like the pages content to model after this one, but the design can be what you come up with. I don't necessarily have to have a color accent line at top of the slide (it seems interfere with page real estate). The pictures will need to be more relevant to IT modernization, transformation, data/AI, digital workforce, consulting. The color team can be white background with light/darker gray, black, ivory and the 2 tones of teals in the logos be the accent. I would use the more muted teal more and the brighter teal to be stronger accent as needed. I found this website template color theme and look and feel to be quite fitting to what I envision
https://www.plumnestsites.com/website-templates/professional-services
Thank you

```html
<!DOCTYPE html>
<html lang="en">
<head>
<meta charset="utf-8">
<title>HQ Lumera – Presentation Template Board</title>
<link href="https://fonts.googleapis.com/css2?family=Jost:ital,wght@0,300;0,400;0,500;0,600;1,300;1,400&display=swap" rel="stylesheet">
<style>
  :root{
    --board:#9b9b9b;
    --teal:#237a7c;
    --teal-deep:#1b6a6d;
    --teal-muted:#2f5e6b;
    --teal-bright:#2aa3a1;
    --ink:#0d0d0d;
    --gray-light:#f1f2f2;
    --gray-text:#6f7578;
    --white:#ffffff;
  }
  *{margin:0;padding:0;box-sizing:border-box}
  html,body{width:702px;height:1200px;overflow:hidden;background:var(--board)}
  body{position:relative;font-family:"Jost",Arial,sans-serif}
  .slide{position:absolute;display:block;filter:drop-shadow(0 3px 4px rgba(0,0,0,.35))}
  .hero-back{left:348px;top:30px;width:329px;height:185px}
  .hero-front{left:28px;top:50px;width:405px;height:228px}
  .thumb{width:148px;height:83px}
  svg text{font-family:"Jost",Arial,sans-serif}
  .h{font-size:7px;fill:var(--teal)}
  .lbl{font-size:4px;fill:var(--ink)}
  .cp{font-size:3.2px;fill:var(--copy,#6f7578)}
  .wt{fill:var(--white)}
  .tl{fill:var(--teal)}
  .bk{fill:var(--ink)}
</style>
</head>
<body>

<svg width="0" height="0" style="position:absolute" aria-hidden="true">
  <defs>
    <linearGradient id="grad-teal" x1="0" y1="0" x2="1" y2="1">
      <stop offset="0" stop-color="#2a8486"/><stop offset="1" stop-color="#1b6a6d"/>
    </linearGradient>
    <linearGradient id="grad-slate" x1="0" y1="0" x2="1" y2="1">
      <stop offset="0" stop-color="#356775"/><stop offset="1" stop-color="#2a5462"/>
    </linearGradient>
    <linearGradient id="grad-night" x1="0" y1="0" x2="1" y2="0">
      <stop offset="0" stop-color="#1e4a50"/><stop offset=".6" stop-color="#0d0d0d"/>
    </linearGradient>
    <linearGradient id="grad-night-slate" x1="0" y1="0" x2="1" y2="0">
      <stop offset="0" stop-color="#2c4757"/><stop offset=".6" stop-color="#0d0d0d"/>
    </linearGradient>
    <linearGradient id="photo-city" x1="0" y1="0" x2="1" y2="1">
      <stop offset="0" stop-color="#c9d6e2"/><stop offset=".5" stop-color="#3d5f86"/><stop offset="1" stop-color="#17263a"/>
    </linearGradient>
    <linearGradient id="photo-office" x1="0" y1="0" x2="1" y2="1">
      <stop offset="0" stop-color="#e6e3dc"/><stop offset="1" stop-color="#8e9aa3"/>
    </linearGradient>
    <linearGradient id="photo-tech" x1="0" y1="0" x2="1" y2="1">
      <stop offset="0" stop-color="#8fb3c9"/><stop offset="1" stop-color="#2a4a63"/>
    </linearGradient>

    <!-- body copy blocks -->
    <g id="copy-two" class="cp">
      <text y="0">Lorem ipsum dolor sit amet,</text>
      <text y="4.3">consectetuer adipiscing elit.</text>
    </g>
    <g id="copy-three" class="cp">
      <text y="0">Lorem ipsum dolor sit amet,</text>
      <text y="4.3">consectetuer adipiscing elit.</text>
      <text y="8.6">Maecenas porttitor congue.</text>
    </g>
    <g id="copy-mid" class="cp">
      <text y="0">Lorem ipsum dolor sit amet, consectetuer adipiscing</text>
      <text y="4.3">elit. Maecenas porttitor congue massa. Fusce posuere,</text>
      <text y="8.6">magna sed pulvinar ultricies purus.</text>
    </g>
    <g id="copy-narrow" class="cp">
      <text y="0">Full spectrum of cloud</text>
      <text y="4.3">services, from planning</text>
      <text y="8.6">to architecture design</text>
      <text y="12.9">and managed delivery.</text>
    </g>
    <g id="copy-long" class="cp">
      <text y="0">Lorem ipsum dolor sit amet, consectetuer adipiscing elit. Maecenas porttitor</text>
      <text y="4.3">congue massa. Fusce posuere, magna sed pulvinar ultricies, purus lectus</text>
      <text y="8.6">malesuada libero, sit amet commodo magna eros quis urna. Nunc viverra</text>
      <text y="12.9">imperdiet enim. Fusce est. Vivamus a tellus. Pellentesque habitant morbi</text>
      <text y="17.2">tristique senectus et netus et malesuada fames ac turpis egestas. Proin</text>
      <text y="21.5">pharetra nonummy pede. Mauris et orci.</text>
    </g>
    <g id="copy-wide" class="cp">
      <text y="0">Lorem ipsum dolor sit amet, consectetuer adipiscing elit. Maecenas porttitor congue massa. Fusce posuere, magna sed pulvinar ultricies, purus lectus</text>
      <text y="4.3">malesuada libero, sit amet commodo magna eros quis urna. Nunc viverra imperdiet enim. Fusce est. Vivamus a tellus. Pellentesque habitant morbi tristique</text>
      <text y="8.6">senectus et netus et malesuada fames ac turpis egestas. Proin pharetra nonummy pede. Mauris et orci. Aenean nec lorem.</text>
    </g>
    <g id="copy-bullet" class="cp">
      <text y="0">Lorem ipsum dolor sit amet, consectetuer adipiscing elit. Maecenas porttitor congue massa, fusce posuere magna sed pulvinar ultricies purus lectus.</text>
    </g>
    <g id="copy-column" class="cp">
      <text y="0">Lorem ipsum is simply</text>
      <text y="4.3">dummy text of the</text>
      <text y="8.6">printing and</text>
      <text y="12.9">typesetting industry.</text>
    </g>

    <!-- content slide frame -->
    <g id="chrome">
      <rect width="310" height="174" fill="#ffffff"/>
      <rect x="5" y="12.5" width="6" height="6" fill="#237a7c"/>
      <text x="271" y="14" font-size="4.2" fill="#2f5e6b">HQ LUMERA</text>
      <rect x="0" y="168" width="160" height="1.6" fill="#237a7c"/>
      <polygon points="150,174 158,166 310,166 310,174" fill="#0d0d0d"/>
      <text x="170" y="171.5" font-size="2.6" fill="#ffffff">2024 All copyright and trademark right reserved</text>
    </g>

    <g id="social">
      <rect x="1" y="1" width="20" height="20" rx="2" fill="none" stroke="#fff" stroke-width="1.4"/>
      <rect x="30" y="1" width="20" height="20" rx="2" fill="none" stroke="#fff" stroke-width="1.4"/>
      <rect x="59" y="1" width="20" height="20" rx="2" fill="none" stroke="#fff" stroke-width="1.4"/>
    </g>
    <g id="social-dark">
      <rect x="1" y="1" width="20" height="20" rx="2" fill="none" stroke="#333" stroke-width="1.4"/>
      <rect x="30" y="1" width="20" height="20" rx="2" fill="none" stroke="#333" stroke-width="1.4"/>
      <rect x="59" y="1" width="20" height="20" rx="2" fill="none" stroke="#333" stroke-width="1.4"/>
    </g>
  </defs>
</svg>

<!-- ============ HERO SLIDES ============ -->
<svg class="slide hero-back" viewBox="0 0 691 388" role="group" aria-label="Title slide, slate variant">
  <rect width="691" height="388" fill="url(#grad-slate)"/>
  <text x="383" y="168" font-size="22" class="wt">HQ LUMERA</text>
  <text x="383" y="210" font-size="21" class="wt">PRESENTATION TITLE</text>
  <text x="383" y="235" font-size="21" class="wt">HERE</text>
  <text x="383" y="260" font-size="10.5" class="wt" font-style="italic" font-weight="300">Our Mission Is To Help Our Clients Accelerate Their</text>
  <text x="383" y="273" font-size="10.5" class="wt" font-style="italic" font-weight="300">Business And Digital Transformation Journey With</text>
  <text x="383" y="286" font-size="10.5" class="wt" font-style="italic" font-weight="300">Precision, And Lasting Impacts.</text>
  <use href="#social" transform="translate(590 346) scale(.875)"/>
</svg>

<svg class="slide hero-front" viewBox="0 0 851 480" role="group" aria-label="Title slide, teal variant">
  <rect width="851" height="480" fill="url(#grad-teal)"/>
  <text x="472" y="205" font-size="28" class="wt">HQ LUMERA</text>
  <text x="472" y="258" font-size="26" class="wt">PRESENTATION TITLE</text>
  <text x="472" y="289" font-size="26" class="wt">HERE</text>
  <text x="472" y="320" font-size="13" class="wt" font-style="italic" font-weight="300">Our Mission Is To Help Our Clients Accelerate Their</text>
  <text x="472" y="336" font-size="13" class="wt" font-style="italic" font-weight="300">Business And Digital Transformation Journey With</text>
  <text x="472" y="352" font-size="13" class="wt" font-style="italic" font-weight="300">Precision, And Lasting Impacts.</text>
  <use href="#social" transform="translate(727 427) scale(1.03)"/>
</svg>

<!-- ============ ROW 1 ============ -->
<svg class="slide thumb" style="left:28px;top:320px" viewBox="0 0 310 174" role="group" aria-label="Title slide teal">
  <rect width="310" height="174" fill="url(#grad-teal)"/>
  <text x="172" y="73" font-size="7.5" class="wt">HQ LUMERA</text>
  <text x="172" y="91" font-size="7" class="wt">PRESENTATION TITLE</text>
  <text x="172" y="100" font-size="7" class="wt">HERE</text>
  <text x="172" y="109" font-size="3.4" class="wt" font-style="italic">Our Mission Is To Help Our Clients Accelerate Their</text>
  <text x="172" y="113" font-size="3.4" class="wt" font-style="italic">Business And Digital Transformation Journey With</text>
  <text x="172" y="117" font-size="3.4" class="wt" font-style="italic">Precision, And Lasting Impacts.</text>
  <use href="#social" transform="translate(264 154) scale(.37)"/>
</svg>

<svg class="slide thumb" style="left:194px;top:320px" viewBox="0 0 310 174" role="group" aria-label="Title slide black">
  <rect width="310" height="174" fill="url(#grad-night)"/>
  <text x="162" y="80" font-size="7.5" class="wt">HQ LUMERA</text>
  <text x="162" y="98" font-size="7" class="wt">PRESENTATION TITLE HERE</text>
  <text x="162" y="106" font-size="3.4" fill="#2aa3a1" font-style="italic">Our Mission Is To Help Our Clients Accelerate Their</text>
  <text x="162" y="110" font-size="3.4" fill="#2aa3a1" font-style="italic">Business And Digital Transformation Journey With</text>
  <text x="162" y="114" font-size="3.4" fill="#2aa3a1" font-style="italic">Precision, And Lasting Impacts.</text>
  <use href="#social" transform="translate(270 150) scale(.35)"/>
</svg>

<svg class="slide thumb" style="left:360px;top:320px" viewBox="0 0 310 174" role="group" aria-label="Title slide white with photo">
  <rect width="310" height="174" fill="#ffffff"/>
  <rect x="170" y="0" width="140" height="174" fill="url(#photo-city)" role="img" aria-label="Office towers photo"/>
  <text x="18" y="78" font-size="7.5" class="tl">HQ LUMERA</text>
  <text x="18" y="93" font-size="7" class="bk">PRESENTATION TITLE HERE</text>
  <text x="18" y="102" font-size="3.4" fill="#555">Our Mission Is To Help Our Clients Accelerate</text>
  <text x="18" y="106" font-size="3.4" fill="#555">Their Business And Digital Transformation Journey</text>
  <text x="18" y="110" font-size="3.4" fill="#555">With Precision, And Lasting Impacts.</text>
  <use href="#social-dark" transform="translate(76 155) scale(.35)"/>
</svg>

<svg class="slide thumb" style="left:526px;top:320px" viewBox="0 0 310 174" role="group" aria-label="Title slide white with photo">
  <rect width="310" height="174" fill="#ffffff"/>
  <rect x="0" y="0" width="150" height="174" fill="url(#photo-city)" role="img" aria-label="Glass skyscraper photo"/>
  <text x="163" y="80" font-size="7.5" class="bk">HQ LUMERA</text>
  <text x="163" y="98" font-size="7" class="bk">PRESENTATION TITLE HERE</text>
  <text x="163" y="107" font-size="3.4" class="tl" font-style="italic">Our Mission Is To Help Our Clients Accelerate Their</text>
  <text x="163" y="111" font-size="3.4" class="tl" font-style="italic">Business And Digital Transformation Journey</text>
  <text x="163" y="115" font-size="3.4" class="tl" font-style="italic">With Precision, And Lasting Impacts.</text>
  <use href="#social-dark" transform="translate(268 155) scale(.35)"/>
</svg>

<!-- ============ ROW 2 ============ -->
<svg class="slide thumb" style="left:28px;top:417px" viewBox="0 0 310 174" role="group" aria-label="Title slide black slate">
  <rect width="310" height="174" fill="url(#grad-night-slate)"/>
  <text x="162" y="84" font-size="7.5" class="wt">HQ LUMERA</text>
  <text x="162" y="102" font-size="7" class="wt">PRESENTATION TITLE HERE</text>
  <text x="162" y="111" font-size="3.4" fill="#4f7588" font-style="italic">Our Mission Is To Help Our Clients Accelerate Their</text>
  <text x="162" y="115" font-size="3.4" fill="#4f7588" font-style="italic">Business And Digital Transformation Journey With</text>
  <text x="162" y="119" font-size="3.4" fill="#4f7588" font-style="italic">Precision, And Lasting Impacts.</text>
  <use href="#social" transform="translate(268 144) scale(.35)"/>
</svg>

<svg class="slide thumb" style="left:194px;top:417px" viewBox="0 0 310 174" role="group" aria-label="Title slide slate">
  <rect width="310" height="174" fill="url(#grad-slate)"/>
  <text x="172" y="73" font-size="7.5" class="wt">HQ LUMERA</text>
  <text x="172" y="91" font-size="7" class="wt">PRESENTATION TITLE</text>
  <text x="172" y="100" font-size="7" class="wt">HERE</text>
  <text x="172" y="109" font-size="3.4" class="wt" font-style="italic">Our Mission Is To Help Our Clients Accelerate Their</text>
  <text x="172" y="113" font-size="3.4" class="wt" font-style="italic">Business And Digital Transformation Journey With</text>
  <text x="172" y="117" font-size="3.4" class="wt" font-style="italic">Precision, And Lasting Impacts.</text>
  <use href="#social" transform="translate(264 154) scale(.37)"/>
</svg>

<svg class="slide thumb" style="left:360px;top:417px" viewBox="0 0 310 174" role="group" aria-label="Agenda slide">
  <use href="#chrome"/>
  <rect x="190" y="0" width="120" height="164" fill="url(#photo-city)" role="img" aria-label="Office towers photo"/>
  <g class="lbl" text-anchor="end">
    <text x="118" y="13">Lorem Ipsum is simply dummy text</text>
    <text x="107" y="35">Lorem Ipsum is simply dummy text</text>
    <text x="96" y="57">Lorem Ipsum is simply dummy text</text>
    <text x="84" y="80">Lorem Ipsum is simply dummy text</text>
  </g>
  <use href="#copy-two" x="118" y="18" style="text-anchor:end"/>
  <use href="#copy-two" x="107" y="40" style="text-anchor:end"/>
  <use href="#copy-two" x="96" y="62" style="text-anchor:end"/>
  <use href="#copy-two" x="84" y="85" style="text-anchor:end"/>
  <circle cx="132" cy="14" r="7" fill="#fff" stroke="#ccc" stroke-width=".6"/><text x="132" y="16" font-size="4.5" text-anchor="middle" class="bk">01</text>
  <circle cx="121" cy="36" r="7" fill="#fff" stroke="#ccc" stroke-width=".6"/><text x="121" y="38" font-size="4.5" text-anchor="middle" class="bk">02</text>
  <circle cx="110" cy="58" r="7" fill="#237a7c"/><text x="110" y="60" font-size="4.5" text-anchor="middle" class="wt">03</text>
  <circle cx="98" cy="81" r="7" fill="#fff" stroke="#ccc" stroke-width=".6"/><text x="98" y="83" font-size="4.5" text-anchor="middle" class="bk">04</text>
  <polygon points="170,100 240,100 230,150 160,150" fill="#237a7c"/>
  <text x="200" y="130" font-size="6.5" text-anchor="middle" class="wt">Agenda</text>
  <text x="200" y="137" font-size="3" text-anchor="middle" class="wt">Lorem ipsum dolor sit</text>
</svg>

<svg class="slide thumb" style="left:526px;top:417px" viewBox="0 0 310 174" role="group" aria-label="Vision mission and core value">
  <use href="#chrome"/>
  <text x="16" y="19" class="h">VISION MISSION AND CORE VALUE</text>
  <polygon points="20,150 80,70 175,70 115,150" fill="#2f5e6b"/>
  <polygon points="40,150 95,80 160,80 205,115 145,115 120,150" fill="#237a7c"/>
  <polygon points="60,150 90,115 200,115 212,132 200,150" fill="#0d0d0d"/>
  <polygon points="80,70 120,42 180,42 175,70" fill="#2aa3a1"/>
  <circle cx="47" cy="140" r="7" fill="#fff"/><circle cx="78" cy="123" r="7" fill="#fff"/><circle cx="113" cy="100" r="7" fill="#fff"/>
  <text x="128" y="60" font-size="4" class="wt">VISION</text>
  <text x="150" y="98" font-size="4" class="wt">MISSION</text>
  <text x="162" y="134" font-size="4" class="wt">CORE VALUES</text>
  <use href="#copy-mid" x="214" y="38"/>
  <use href="#copy-mid" x="214" y="78"/>
  <use href="#copy-mid" x="214" y="118"/>
</svg>

<!-- ============ ROW 3 ============ -->
<svg class="slide thumb" style="left:28px;top:514px" viewBox="0 0 310 174" role="group" aria-label="Heading slide with photo">
  <use href="#chrome"/>
  <text x="16" y="19" class="h">HEADING GOES HERE</text>
  <rect x="110" y="35" width="200" height="120" fill="#f1f2f2"/>
  <polygon points="0,35 135,35 115,160 0,160" fill="url(#photo-office)" role="img" aria-label="Team working at laptops photo"/>
  <use href="#copy-long" x="148" y="48"/>
  <use href="#copy-long" x="148" y="82"/>
</svg>

<svg class="slide thumb" style="left:194px;top:514px" viewBox="0 0 310 174" role="group" aria-label="Heading slide with desk photo">
  <use href="#chrome"/>
  <text x="16" y="19" class="h">HEADING GOES HERE</text>
  <rect x="160" y="0" width="150" height="120" fill="url(#photo-office)" role="img" aria-label="Consultant reviewing charts photo"/>
  <use href="#copy-long" x="14" y="30"/>
  <use href="#copy-two" x="14" y="60"/>
  <circle cx="22" cy="102" r="6" fill="#fff" stroke="#ccc" stroke-width=".6"/><text x="22" y="104" font-size="4" text-anchor="middle" class="tl">01</text>
  <circle cx="22" cy="130" r="6" fill="#fff" stroke="#ccc" stroke-width=".6"/><text x="22" y="132" font-size="4" text-anchor="middle" class="tl">02</text>
  <text x="36" y="98" class="lbl">Text here</text><use href="#copy-two" x="36" y="103"/>
  <text x="36" y="126" class="lbl">Text here</text><use href="#copy-two" x="36" y="131"/>
  <polygon points="232,82 305,82 305,130 222,130" fill="#237a7c"/>
  <text x="298" y="103" font-size="4" class="wt" text-anchor="end">Text here</text>
  <text x="298" y="110" font-size="2.8" class="wt" text-anchor="end">Simply random text here.</text>
  <text x="298" y="114" font-size="2.8" class="wt" text-anchor="end">It has roots in classical Latin.</text>
</svg>

<svg class="slide thumb" style="left:360px;top:514px" viewBox="0 0 310 174" role="group" aria-label="Problem slide">
  <use href="#chrome"/>
  <text x="16" y="19" class="h">PROBLEM SLIDES</text>
  <path d="M55,50 A42,42 0 1,0 97,92" fill="none" stroke="#237a7c" stroke-width="2"/>
  <circle cx="55" cy="92" r="36" fill="#f1f2f2"/>
  <circle cx="55" cy="92" r="28" fill="#0d0d0d"/>
  <text x="55" y="104" font-size="34" text-anchor="middle" class="wt">?</text>
  <g fill="#237a7c"><circle cx="117" cy="48" r="2"/><circle cx="117" cy="76" r="2"/><circle cx="117" cy="104" r="2"/><circle cx="117" cy="132" r="2"/></g>
  <g font-size="3.8" class="tl"><text x="127" y="45">Text Here</text><text x="127" y="73">Text Here</text><text x="127" y="101">Text Here</text><text x="127" y="129" fill="#999">Text Here</text></g>
  <use href="#copy-mid" x="127" y="51"/>
  <use href="#copy-mid" x="127" y="79"/>
  <use href="#copy-mid" x="127" y="107"/>
  <use href="#copy-mid" x="127" y="135"/>
</svg>

<svg class="slide thumb" style="left:526px;top:514px" viewBox="0 0 310 174" role="group" aria-label="Solution slide">
  <use href="#chrome"/>
  <text x="16" y="19" class="h">SOLUTION SLIDES</text>
  <rect x="130" y="72" width="55" height="14" rx="7" fill="#237a7c"/>
  <rect x="133" y="88" width="49" height="12" fill="#7a8a90"/>
  <rect x="138" y="102" width="39" height="11" fill="#2f5e6b"/>
  <rect x="144" y="115" width="27" height="8" fill="#333"/>
  <rect x="150" y="125" width="15" height="6" rx="2" fill="#111"/>
  <g fill="#fff" stroke="#aab" stroke-width=".8">
    <circle cx="128" cy="46" r="7"/><circle cx="175" cy="46" r="7"/><circle cx="102" cy="80" r="7"/><circle cx="210" cy="80" r="7"/><circle cx="104" cy="120" r="7"/><circle cx="200" cy="122" r="7"/>
  </g>
  <g fill="#237a7c"><circle cx="175" cy="46" r="4"/><circle cx="210" cy="80" r="4"/><circle cx="200" cy="122" r="4"/></g>
  <g class="lbl"><text x="116" y="40" text-anchor="end">Text Here</text><text x="90" y="74" text-anchor="end">Text Here</text><text x="92" y="114" text-anchor="end">Text Here</text>
  <text x="188" y="40">Text Here</text><text x="222" y="74">Text Here</text><text x="212" y="116">Text Here</text></g>
  <use href="#copy-two" x="116" y="45" style="text-anchor:end"/>
  <use href="#copy-two" x="90" y="79" style="text-anchor:end"/>
  <use href="#copy-two" x="92" y="119" style="text-anchor:end"/>
  <use href="#copy-two" x="188" y="45"/>
  <use href="#copy-two" x="222" y="79"/>
  <use href="#copy-two" x="212" y="121"/>
</svg>

<!-- ============ ROW 4 ============ -->
<svg class="slide thumb" style="left:28px;top:611px" viewBox="0 0 310 174" role="group" aria-label="Heading slide with circles">
  <use href="#chrome"/>
  <text x="16" y="19" class="h">HEADING GOES HERE</text>
  <polygon points="150,20 230,20 170,160 100,160" fill="#f1f2f2"/>
  <use href="#copy-long" x="14" y="28"/>
  <g class="lbl" font-style="italic"><text x="26" y="82">Description</text><text x="26" y="103">Description</text><text x="26" y="124">Description</text></g>
  <g fill="#237a7c"><circle cx="20" cy="81" r="2"/><circle cx="20" cy="102" r="2"/><circle cx="20" cy="123" r="2"/></g>
  <use href="#copy-two" x="26" y="87"/><use href="#copy-two" x="26" y="108"/><use href="#copy-two" x="26" y="129"/>
  <circle cx="210" cy="55" r="32" fill="url(#photo-tech)" role="img" aria-label="Business handshake photo"/>
  <circle cx="258" cy="100" r="22" fill="url(#photo-office)" role="img" aria-label="Team meeting photo"/>
  <circle cx="188" cy="135" r="22" fill="url(#photo-office)" role="img" aria-label="Analytics dashboard photo"/>
  <circle cx="168" cy="38" r="9" fill="#2f5e6b"/><text x="168" y="40" font-size="5" text-anchor="middle" class="wt">675</text>
  <circle cx="214" cy="145" r="9" fill="#fff" stroke="#ccc" stroke-width=".6"/><text x="214" y="147" font-size="5" text-anchor="middle" class="bk">458</text>
</svg>

<svg class="slide thumb" style="left:194px;top:611px" viewBox="0 0 310 174" role="group" aria-label="Section slide 01">
  <rect width="310" height="174" fill="#ffffff"/>
  <rect x="0" y="0" width="150" height="174" fill="#0d0d0d"/>
  <polygon points="140,28 310,28 310,95 130,95" fill="#2f5e6b"/>
  <text x="160" y="58" font-size="11" class="wt">01</text>
  <text x="160" y="72" font-size="8" class="wt">SECTION SLIDE</text>
  <text x="160" y="84" font-size="3.6" class="wt">Lorem ipsum dolor sit amet, consectetuer adipiscing elit.</text>
  <text x="240" y="155" font-size="9" class="bk">HQ LUMERA</text>
</svg>

<svg class="slide thumb" style="left:360px;top:611px" viewBox="0 0 310 174" role="group" aria-label="Three photo cards">
  <use href="#chrome"/>
  <text x="16" y="19" class="h">TITLE GOES HERE</text>
  <rect x="40" y="30" width="74" height="40" fill="url(#photo-office)" role="img" aria-label="Team discussion photo"/>
  <rect x="124" y="30" width="74" height="40" fill="url(#photo-office)" role="img" aria-label="Office collaboration photo"/>
  <rect x="208" y="30" width="74" height="40" fill="url(#photo-office)" role="img" aria-label="Client meeting photo"/>
  <g font-size="4" class="tl"><text x="44" y="82">Heading Here</text><text x="128" y="82">Heading Here</text><text x="212" y="82">Heading Here</text></g>
  <use href="#copy-three" x="44" y="89"/><use href="#copy-three" x="128" y="89"/><use href="#copy-three" x="212" y="89"/>
  <use href="#copy-three" x="44" y="104"/><use href="#copy-three" x="128" y="104"/><use href="#copy-three" x="212" y="104"/>
  <g fill="#0d0d0d"><rect x="106" y="142" width="8" height="8"/><rect x="190" y="142" width="8" height="8"/><rect x="274" y="142" width="8" height="8"/></g>
</svg>

<svg class="slide thumb" style="left:526px;top:611px" viewBox="0 0 310 174" role="group" aria-label="Title slide with black icon band">
  <use href="#chrome"/>
  <polygon points="0,0 155,0 130,90 0,90" fill="#f1f2f2"/>
  <polygon points="40,10 140,10 120,80 20,80" fill="url(#photo-tech)" role="img" aria-label="Hand holding digital city hologram photo"/>
  <polygon points="0,90 160,90 145,140 0,140" fill="#0d0d0d"/>
  <g fill="none" stroke="#fff" stroke-width="1"><circle cx="30" cy="108" r="5"/><circle cx="70" cy="108" r="5"/><circle cx="110" cy="108" r="5"/></g>
  <g font-size="3" fill="#8aa" text-anchor="middle"><text x="30" y="124">Your text</text><text x="70" y="124">Your text</text><text x="110" y="124">Your text</text></g>
  <rect x="154" y="28" width="5" height="5" fill="#237a7c"/>
  <text x="163" y="33" class="h">TITLE GOES HERE</text>
  <use href="#copy-long" x="163" y="44"/>
  <use href="#copy-long" x="163" y="78"/>
</svg>

<!-- ============ ROW 5 ============ -->
<svg class="slide thumb" style="left:28px;top:708px" viewBox="0 0 310 174" role="group" aria-label="Key figures slide">
  <use href="#chrome"/>
  <text x="16" y="19" class="h">TITLE GOES HERE</text>
  <circle cx="60" cy="70" r="28" fill="#2f5e6b"/><text x="60" y="74" font-size="10" text-anchor="middle" class="wt">6.6 M</text>
  <circle cx="127" cy="70" r="28" fill="#237a7c"/><text x="127" y="74" font-size="10" text-anchor="middle" class="wt">5.3 M</text>
  <circle cx="194" cy="70" r="28" fill="#2aa3a1"/><text x="194" y="74" font-size="10" text-anchor="middle" class="wt">3.9 M</text>
  <circle cx="261" cy="70" r="20" fill="#0d0d0d"/><text x="261" y="74" font-size="9" text-anchor="middle" class="wt">85%</text>
  <g class="lbl" text-anchor="middle"><text x="60" y="116">Market Capacity</text><text x="127" y="116">Market Potential</text><text x="194" y="116">Market Volume</text><text x="261" y="116">Market Share</text></g>
  <g style="text-anchor:middle">
    <use href="#copy-three" x="60" y="124"/><use href="#copy-three" x="127" y="124"/><use href="#copy-three" x="194" y="124"/><use href="#copy-three" x="261" y="124"/>
  </g>
</svg>

<svg class="slide thumb" style="left:194px;top:708px" viewBox="0 0 310 174" role="group" aria-label="Six numbered points slide">
  <use href="#chrome"/>
  <text x="16" y="19" class="h">TITLE GOES HERE</text>
  <rect x="0" y="30" width="45" height="120" fill="url(#photo-tech)" role="img" aria-label="Analyst with charts photo"/>
  <polygon points="45,30 62,30 62,150 30,150" fill="#0d0d0d"/>
  <g fill="#fff" stroke="#ccc" stroke-width=".6">
    <circle cx="100" cy="42" r="5"/><circle cx="170" cy="42" r="5"/><circle cx="240" cy="42" r="5"/>
    <circle cx="100" cy="100" r="5"/><circle cx="170" cy="100" r="5"/><circle cx="240" cy="100" r="5"/>
  </g>
  <g font-size="3.5" text-anchor="middle" class="tl"><text x="100" y="43.5">01</text><text x="170" y="43.5">02</text><text x="240" y="43.5">03</text><text x="100" y="101.5">04</text><text x="170" y="101.5">05</text><text x="240" y="101.5">06</text></g>
  <g font-size="3.8" class="tl"><text x="90" y="57">Your title here</text><text x="160" y="57">Your title here</text><text x="230" y="57">Your title here</text><text x="90" y="115">Your title here</text><text x="160" y="115">Your title here</text><text x="230" y="115">Your title here</text></g>
  <use href="#copy-three" x="90" y="63"/><use href="#copy-three" x="160" y="63"/><use href="#copy-three" x="230" y="63"/>
  <use href="#copy-three" x="90" y="121"/><use href="#copy-three" x="160" y="121"/><use href="#copy-three" x="230" y="121"/>
</svg>

<svg class="slide thumb" style="left:360px;top:708px" viewBox="0 0 310 174" role="group" aria-label="Table slide">
  <use href="#chrome"/>
  <text x="16" y="19" class="h">TABLE SLIDE</text>
  <rect x="72" y="32" width="225" height="12" fill="#0d0d0d"/>
  <g font-size="4.2" class="wt" text-anchor="middle"><text x="100" y="40">Option 1</text><text x="156" y="40">Option 2</text><text x="212" y="40">Option 3</text><text x="268" y="40">Option 4</text></g>
  <g fill="none" stroke="#bbb" stroke-width=".5">
    <rect x="14" y="44" width="283" height="86"/>
    <line x1="14" y1="61" x2="297" y2="61"/><line x1="14" y1="78" x2="297" y2="78"/><line x1="14" y1="95" x2="297" y2="95"/><line x1="14" y1="112" x2="297" y2="112"/>
    <line x1="72" y1="44" x2="72" y2="130"/>
  </g>
  <g class="lbl" font-size="3.6"><text x="20" y="54">Lorem Ipsum</text><text x="20" y="71">Lorem Ipsum</text><text x="20" y="88">Lorem Ipsum</text><text x="20" y="105">Lorem Ipsum</text><text x="20" y="122">Lorem Ipsum</text></g>
  <g fill="#237a7c">
    <rect x="98" y="49" width="5" height="5"/><rect x="154" y="49" width="5" height="5"/>
    <rect x="98" y="66" width="5" height="5"/><rect x="154" y="66" width="5" height="5"/><rect x="210" y="66" width="5" height="5"/><rect x="266" y="66" width="5" height="5"/>
    <rect x="98" y="83" width="5" height="5"/><rect x="154" y="83" width="5" height="5"/><rect x="266" y="83" width="5" height="5"/>
    <rect x="98" y="100" width="5" height="5"/><rect x="154" y="100" width="5" height="5"/><rect x="210" y="100" width="5" height="5"/>
    <rect x="98" y="117" width="5" height="5"/><rect x="154" y="117" width="5" height="5"/><rect x="210" y="117" width="5" height="5"/><rect x="266" y="117" width="5" height="5"/>
  </g>
  <use href="#copy-wide" x="14" y="140"/>
</svg>

<svg class="slide thumb" style="left:526px;top:708px" viewBox="0 0 310 174" role="group" aria-label="Business transformation offerings">
  <use href="#chrome"/>
  <text x="16" y="19" class="h">BUSINESS TRANSFORMATION OFFERINGS</text>
  <g fill="#fff" stroke="#e2e4e4" stroke-width=".8">
    <rect x="18" y="30" width="62" height="120"/><rect x="90" y="30" width="62" height="120"/><rect x="162" y="30" width="62" height="120"/><rect x="234" y="30" width="62" height="120"/>
  </g>
  <g fill="#fff" stroke="#0d0d0d" stroke-width="1.4"><circle cx="49" cy="42" r="9"/><circle cx="121" cy="42" r="9"/><circle cx="193" cy="42" r="9"/><circle cx="265" cy="42" r="9"/></g>
  <g fill="#237a7c"><circle cx="49" cy="42" r="4"/><circle cx="121" cy="42" r="4"/><circle cx="193" cy="42" r="4"/><circle cx="265" cy="42" r="4"/></g>
  <g class="lbl" font-size="3.4" text-anchor="middle" font-weight="600">
    <text x="49" y="62">Scaled Agile Delivery</text><text x="121" y="62">Project Management</text><text x="193" y="62">Strategy and Business</text><text x="265" y="62">Business Process</text>
  </g>
  <g style="text-anchor:middle">
    <use href="#copy-narrow" x="49" y="72"/><use href="#copy-narrow" x="121" y="72"/><use href="#copy-narrow" x="193" y="72"/><use href="#copy-narrow" x="265" y="72"/>
    <use href="#copy-narrow" x="121" y="92"/><use href="#copy-narrow" x="193" y="92"/><use href="#copy-narrow" x="265" y="92"/>
  </g>
  <g fill="#0d0d0d"><rect x="72" y="144" width="7" height="7"/><rect x="216" y="144" width="7" height="7"/></g>
  <g fill="#237a7c"><rect x="144" y="144" width="7" height="7"/><rect x="288" y="144" width="7" height="7"/></g>
</svg>

<!-- ============ ROW 6 ============ -->
<svg class="slide thumb" style="left:28px;top:804px" viewBox="0 0 310 174" role="group" aria-label="Digital transformation offerings">
  <use href="#chrome"/>
  <text x="16" y="19" class="h">DIGITAL TRANSFORMATION OFFERINGS</text>
  <rect x="0" y="50" width="310" height="2" fill="#237a7c"/>
  <g fill="#fff" stroke="#0d0d0d" stroke-width="1.2">
    <circle cx="45" cy="51" r="7"/><circle cx="100" cy="51" r="7"/><circle cx="155" cy="51" r="7"/><circle cx="210" cy="51" r="7"/><circle cx="265" cy="51" r="7"/>
  </g>
  <g fill="#237a7c"><circle cx="45" cy="51" r="3"/><circle cx="100" cy="51" r="3"/><circle cx="155" cy="51" r="3"/><circle cx="210" cy="51" r="3"/><circle cx="265" cy="51" r="3"/></g>
  <g class="lbl" font-size="3.4" text-anchor="middle" font-weight="600">
    <text x="45" y="68">Cloud Strategy</text><text x="100" y="68">AI Solutions</text><text x="155" y="68">Data Modernization</text><text x="210" y="68">App Modernization</text><text x="265" y="68">DevSecOps</text>
  </g>
  <g style="text-anchor:middle">
    <use href="#copy-narrow" x="45" y="77"/><use href="#copy-narrow" x="100" y="77"/><use href="#copy-narrow" x="155" y="77"/><use href="#copy-narrow" x="210" y="77"/><use href="#copy-narrow" x="265" y="77"/>
    <use href="#copy-narrow" x="100" y="97"/><use href="#copy-narrow" x="155" y="97"/>
  </g>
</svg>

<svg class="slide thumb" style="left:194px;top:804px" viewBox="0 0 310 174" role="group" aria-label="Section slide 02">
  <rect width="310" height="174" fill="#ffffff"/>
  <rect x="160" y="0" width="150" height="174" fill="#0d0d0d"/>
  <polygon points="0,28 180,28 170,95 0,95" fill="#2f5e6b"/>
  <text x="20" y="58" font-size="11" class="wt">02</text>
  <text x="20" y="72" font-size="8" class="wt">SECTION SLIDE</text>
  <text x="20" y="84" font-size="3.6" class="wt">Lorem ipsum dolor sit amet, consectetuer adipiscing elit.</text>
  <rect x="218" y="143" width="84" height="17" fill="#ffffff"/>
  <text x="224" y="155" font-size="9" class="bk">HQ LUMERA</text>
  <text x="40" y="170" font-size="2.6" fill="#999">2024 All copyright and trademark right reserved</text>
</svg>

<svg class="slide thumb" style="left:360px;top:804px" viewBox="0 0 310 174" role="group" aria-label="Value proposition donut chart">
  <use href="#chrome"/>
  <text x="16" y="19" class="h">VALUE PROPOSITION</text>
  <circle cx="70" cy="90" r="43" fill="#0d0d0d"/>
  <path d="M70,90 L70,47 A43,43 0 0,0 27,88 Z" fill="#237a7c"/>
  <path d="M70,90 L27,88 A43,43 0 0,0 33,112 Z" fill="#9aa3a6"/>
  <path d="M70,90 L33,112 A43,43 0 0,0 46,126 Z" fill="#cfd3d4"/>
  <circle cx="70" cy="90" r="13" fill="#fff"/>
  <circle cx="70" cy="90" r="6" fill="none" stroke="#0d0d0d" stroke-width="1.2"/>
  <g font-size="4.2" class="wt"><text x="42" y="70">20%</text><text x="95" y="100">60%</text><text x="36" y="100">10%</text><text x="46" y="116">10%</text></g>
  <g font-size="4"><text x="150" y="45" class="bk">Description Text</text><text x="225" y="45" class="tl">Description Text</text><text x="150" y="100" class="bk">Description Text</text><text x="225" y="100" fill="#999">Description Text</text></g>
  <use href="#copy-three" x="150" y="52"/><use href="#copy-three" x="225" y="52"/><use href="#copy-three" x="150" y="107"/><use href="#copy-three" x="225" y="107"/>
</svg>

<svg class="slide thumb" style="left:526px;top:804px" viewBox="0 0 310 174" role="group" aria-label="Percentage cards slide">
  <use href="#chrome"/>
  <text x="16" y="20" class="h">TITLE GOES HERE</text>
  <text x="16" y="28" font-size="6.5" class="tl">LOREM IPSUM DOLOR SIT</text>
  <text x="16" y="36" font-size="6.5" class="tl">AMET, CONSECTETUER</text>
  <text x="16" y="44" font-size="6.5" class="tl">ADIPISCING ELIT.</text>
  <use href="#copy-mid" x="160" y="26"/>
  <rect x="16" y="60" width="130" height="38" fill="#fff" stroke="#e2e4e4"/>
  <rect x="160" y="60" width="130" height="38" fill="#0d0d0d"/>
  <rect x="16" y="108" width="130" height="38" fill="#fff" stroke="#e2e4e4"/>
  <rect x="160" y="108" width="130" height="38" fill="#fff" stroke="#e2e4e4"/>
  <g fill="none" stroke-width="2.2">
    <circle cx="33" cy="79" r="9" stroke="#237a7c"/><circle cx="177" cy="79" r="9" stroke="#2aa3a1"/><circle cx="33" cy="127" r="9" stroke="#bbb"/><circle cx="177" cy="127" r="9" stroke="#bbb"/>
  </g>
  <g font-size="4" text-anchor="middle"><text x="33" y="80.5" class="bk">75%</text><text x="177" y="80.5" class="wt">85%</text><text x="33" y="128.5" class="bk">50%</text><text x="177" y="128.5" class="bk">60%</text></g>
  <g font-size="3.8"><text x="50" y="71" class="bk">Your Title Here</text><text x="194" y="71" class="tl">Your Title Here</text><text x="50" y="119" class="bk">Your Title Here</text><text x="194" y="119" class="bk">Your Title Here</text></g>
  <use href="#copy-mid" x="50" y="77" style="font-size:2.8px"/>
  <use href="#copy-mid" x="194" y="77" style="--copy:#c9cccd"/>
  <use href="#copy-mid" x="50" y="125"/>
  <use href="#copy-mid" x="194" y="125"/>
</svg>

<!-- ============ ROW 7 ============ -->
<svg class="slide thumb" style="left:28px;top:902px" viewBox="0 0 310 174" role="group" aria-label="Bar chart slide">
  <use href="#chrome"/>
  <text x="16" y="19" class="h">TITLE GOES HERE</text>
  <rect x="0" y="30" width="150" height="130" fill="#f1f2f2"/>
  <g fill="none" stroke="#ccc" stroke-width=".4"><line x1="20" y1="60" x2="135" y2="60"/><line x1="20" y1="80" x2="135" y2="80"/><line x1="20" y1="100" x2="135" y2="100"/><line x1="20" y1="120" x2="135" y2="120"/></g>
  <g fill="#2f5e6b"><rect x="30" y="90" width="8" height="30"/><rect x="58" y="80" width="8" height="40"/><rect x="86" y="70" width="8" height="50"/><rect x="114" y="60" width="8" height="60"/></g>
  <g fill="#0d0d0d"><rect x="39" y="85" width="8" height="35"/><rect x="67" y="90" width="8" height="30"/><rect x="95" y="80" width="8" height="40"/><rect x="123" y="75" width="8" height="45"/></g>
  <g fill="#237a7c"><rect x="48" y="95" width="6" height="25"/><rect x="76" y="75" width="6" height="45"/><rect x="104" y="85" width="6" height="35"/></g>
  <g font-size="3" fill="#888" text-anchor="middle"><text x="42" y="127">Category 1</text><text x="70" y="127">Category 2</text><text x="98" y="127">Category 3</text><text x="126" y="127">Category 4</text></g>
  <polygon points="150,35 300,35 294,52 150,52" fill="#2f5e6b"/>
  <polygon points="150,72 300,72 294,89 150,89" fill="#0d0d0d"/>
  <polygon points="150,109 300,109 294,126 150,126" fill="#237a7c"/>
  <use href="#copy-two" x="156" y="42" style="--copy:#ffffff"/>
  <use href="#copy-two" x="156" y="79" style="--copy:#ffffff"/>
  <use href="#copy-two" x="156" y="116" style="--copy:#ffffff"/>
  <g fill="#fff"><circle cx="284" cy="43.5" r="3"/><circle cx="284" cy="80.5" r="3"/><circle cx="284" cy="117.5" r="3"/></g>
</svg>

<svg class="slide thumb" style="left:194px;top:902px" viewBox="0 0 310 174" role="group" aria-label="Timeline slide">
  <use href="#chrome"/>
  <text x="16" y="19" class="h">TITLE GOES HERE</text>
  <rect x="150" y="0" width="160" height="55" fill="url(#photo-office)" role="img" aria-label="Consultants signing documents photo"/>
  <rect x="0" y="55" width="310" height="16" fill="#2f5e6b"/>
  <polygon points="0,71 310,71 310,145 30,145" fill="#0d0d0d"/>
  <rect x="12" y="58" width="10" height="10" fill="#fff"/>
  <g font-size="5" class="wt" font-style="italic"><text x="40" y="66">2019</text><text x="90" y="66">2021</text><text x="140" y="66">2022</text><text x="190" y="66">2023</text><text x="240" y="66">2024</text></g>
  <g font-size="4.5" fill="#2aa3a1"><text x="40" y="84">Lorem</text><text x="90" y="84">Lorem</text><text x="140" y="84">Lorem</text><text x="190" y="84">Lorem</text><text x="240" y="84">Lorem</text></g>
  <g style="--copy:#c9cccd">
    <use href="#copy-column" x="40" y="92"/><use href="#copy-column" x="90" y="92"/><use href="#copy-column" x="140" y="92"/><use href="#copy-column" x="190" y="92"/><use href="#copy-column" x="240" y="92"/>
  </g>
</svg>

<svg class="slide thumb" style="left:360px;top:902px" viewBox="0 0 310 174" role="group" aria-label="Horizontal bar chart slide">
  <use href="#chrome"/>
  <text x="16" y="19" class="h">TITLE GOES HERE</text>
  <circle cx="24" cy="50" r="8" fill="#0d0d0d"/><text x="24" y="52" font-size="5" text-anchor="middle" class="wt">01</text>
  <circle cx="24" cy="84" r="8" fill="#9aa3a6"/><text x="24" y="86" font-size="5" text-anchor="middle" class="wt">02</text>
  <circle cx="24" cy="118" r="8" fill="#237a7c"/><text x="24" y="120" font-size="5" text-anchor="middle" class="wt">03</text>
  <g font-size="4" class="bk"><text x="38" y="43">Your First Title Here</text><text x="38" y="77">Your Second Title Here</text><text x="38" y="111">Your Third Title Here</text></g>
  <use href="#copy-mid" x="38" y="49"/><use href="#copy-mid" x="38" y="83"/><use href="#copy-mid" x="38" y="117"/>
  <line x1="170" y1="35" x2="170" y2="138" stroke="#ccc" stroke-width=".5"/>
  <g font-size="3" fill="#999" text-anchor="end"><text x="167" y="47">Category 4</text><text x="167" y="72">Category 3</text><text x="167" y="97">Category 2</text><text x="167" y="122">Category 1</text></g>
  <g fill="#2f5e6b"><rect x="170" y="38" width="110" height="4"/><rect x="170" y="63" width="60" height="4"/><rect x="170" y="88" width="80" height="4"/><rect x="170" y="113" width="50" height="4"/></g>
  <g fill="#9aa3a6"><rect x="170" y="43" width="90" height="4"/><rect x="170" y="68" width="95" height="4"/><rect x="170" y="93" width="70" height="4"/><rect x="170" y="118" width="40" height="4"/></g>
  <g fill="#0d0d0d"><rect x="170" y="48" width="70" height="4"/><rect x="170" y="73" width="40" height="4"/><rect x="170" y="98" width="55" height="4"/><rect x="170" y="123" width="30" height="4"/></g>
</svg>

<svg class="slide thumb" style="left:526px;top:902px" viewBox="0 0 310 174" role="group" aria-label="Two paragraph text slide">
  <use href="#chrome"/>
  <text x="16" y="24" font-size="6.5" class="tl">TWO PARAGRAPH TEXT</text>
  <text x="16" y="32" font-size="6.5" class="tl">ALREADY TO BE CHANGED</text>
  <text x="16" y="40" font-size="6.5" class="tl">WITH YOUR OWN</text>
  <text x="160" y="34" font-size="12" class="bk">“</text>
  <use href="#copy-mid" x="170" y="27" style="--copy:#237a7c"/>
  <use href="#copy-long" x="16" y="56"/><use href="#copy-long" x="16" y="85"/><use href="#copy-long" x="16" y="114"/>
  <use href="#copy-long" x="165" y="56"/><use href="#copy-long" x="165" y="85"/><use href="#copy-long" x="165" y="114"/>
</svg>

<!-- ============ ROW 8 ============ -->
<svg class="slide thumb" style="left:28px;top:998px" viewBox="0 0 310 174" role="group" aria-label="One paragraph text slide">
  <use href="#chrome"/>
  <text x="16" y="21" font-size="6.5" class="tl">ONE PARAGRAPH TEXT</text>
  <text x="16" y="29" font-size="6.5" class="tl">ALREADY TO BE CHANGED</text>
  <text x="16" y="37" font-size="6.5" class="tl">WITH YOUR OWN</text>
  <circle cx="22" cy="55" r="4" fill="#0d0d0d"/>
  <text x="30" y="56.5" font-size="4" class="bk">Subheading Goes Here</text>
  <use href="#copy-wide" x="16" y="68"/>
  <use href="#copy-wide" x="16" y="82"/>
  <use href="#copy-wide" x="16" y="96"/>
  <use href="#copy-wide" x="16" y="110"/>
</svg>

<svg class="slide thumb" style="left:194px;top:998px" viewBox="0 0 310 174" role="group" aria-label="Bullet point slide">
  <use href="#chrome"/>
  <text x="16" y="19" class="h">BULLET POINT SLIDE</text>
  <use href="#copy-wide" x="16" y="32"/>
  <g fill="#0d0d0d">
    <circle cx="19" cy="56" r="1.2"/><circle cx="19" cy="69" r="1.2"/><circle cx="19" cy="82" r="1.2"/><circle cx="19" cy="95" r="1.2"/><circle cx="19" cy="108" r="1.2"/><circle cx="19" cy="121" r="1.2"/><circle cx="19" cy="134" r="1.2"/>
  </g>
  <use href="#copy-bullet" x="24" y="57"/><use href="#copy-bullet" x="24" y="70"/><use href="#copy-bullet" x="24" y="83"/><use href="#copy-bullet" x="24" y="96"/><use href="#copy-bullet" x="24" y="109"/><use href="#copy-bullet" x="24" y="122"/><use href="#copy-bullet" x="24" y="135"/>
</svg>

<svg class="slide thumb" style="left:360px;top:998px" viewBox="0 0 310 174" role="group" aria-label="Meet our experts">
  <use href="#chrome"/>
  <text x="16" y="19" class="h">MEET OUR EXPERTS</text>
  <g fill="#fff" stroke="#e2e4e4" stroke-width=".8">
    <rect x="22" y="30" width="62" height="125"/><rect x="92" y="30" width="62" height="125"/><rect x="162" y="30" width="62" height="125"/><rect x="232" y="30" width="62" height="125"/>
  </g>
  <g fill="#c5c9ca" stroke="#fff" stroke-width="2">
    <circle cx="53" cy="52" r="15" role="img" aria-label="Team member portrait"/><circle cx="123" cy="52" r="15" role="img" aria-label="Team member portrait"/><circle cx="193" cy="52" r="15" role="img" aria-label="Team member portrait"/><circle cx="263" cy="52" r="15" role="img" aria-label="Team member portrait"/>
  </g>
  <g font-size="3.8" text-anchor="middle" class="bk">
    <text x="53" y="82">ODELL</text><text x="53" y="87">FERRIS</text>
    <text x="123" y="82">MIRA</text><text x="123" y="87">QUINTAL</text>
    <text x="193" y="82">JANEK</text><text x="193" y="87">SORVOLD</text>
    <text x="263" y="82">TESSA</text><text x="263" y="87">WYNCOMBE</text>
  </g>
  <g font-size="2.8" text-anchor="middle" class="tl"><text x="53" y="92">Manager Position</text><text x="123" y="92">Manager Position</text><text x="193" y="92">Manager Position</text><text x="263" y="92">Manager Position</text></g>
  <g fill="#237a7c"><rect x="47" y="96" width="3" height="3"/><rect x="52" y="96" width="3" height="3"/><rect x="57" y="96" width="3" height="3"/><rect x="117" y="96" width="3" height="3"/><rect x="122" y="96" width="3" height="3"/><rect x="127" y="96" width="3" height="3"/><rect x="187" y="96" width="3" height="3"/><rect x="192" y="96" width="3" height="3"/><rect x="197" y="96" width="3" height="3"/><rect x="257" y="96" width="3" height="3"/><rect x="262" y="96" width="3" height="3"/><rect x="267" y="96" width="3" height="3"/></g>
  <g style="text-anchor:middle;font-size:2.9px">
    <use href="#copy-three" x="53" y="108"/><use href="#copy-three" x="123" y="108"/><use href="#copy-three" x="193" y="108"/><use href="#copy-three" x="263" y="108"/>
  </g>
</svg>

<svg class="slide thumb" style="left:526px;top:998px" viewBox="0 0 310 174" role="group" aria-label="Expert in details">
  <use href="#chrome"/>
  <rect x="0" y="0" width="130" height="60" fill="#0d0d0d"/>
  <circle cx="70" cy="75" r="40" fill="#c5c9ca" role="img" aria-label="Expert portrait"/>
  <text x="30" y="118" font-size="16" fill="#2f5e6b">”</text>
  <text x="155" y="40" font-size="6" class="bk">EXPERT IN DETAILS</text>
  <text x="155" y="47" font-size="3.4" class="tl" font-style="italic">Lorem ipsum is simply dummy text</text>
  <use href="#copy-mid" x="155" y="55"/>
  <g font-size="3" fill="#999"><text x="155" y="94">Description</text><text x="155" y="108">Description</text><text x="155" y="122">Description</text></g>
  <g fill="#d8dbdc"><rect x="155" y="96" width="120" height="1.5"/><rect x="155" y="110" width="120" height="1.5"/><rect x="155" y="124" width="120" height="1.5"/></g>
  <rect x="155" y="96" width="92" height="1.5" fill="#0d0d0d"/><rect x="155" y="110" width="100" height="1.5" fill="#237a7c"/><rect x="155" y="124" width="80" height="1.5" fill="#0d0d0d"/>
  <g fill="#0d0d0d"><circle cx="247" cy="96.7" r="1.8"/><circle cx="255" cy="110.7" r="1.8"/><circle cx="235" cy="124.7" r="1.8"/></g>
  <g font-size="3" fill="#999"><text x="282" y="98">85%</text><text x="282" y="112">90%</text><text x="282" y="126">80%</text></g>
</svg>

<!-- ============ ROW 9 ============ -->
<svg class="slide thumb" style="left:28px;top:1095px" viewBox="0 0 310 174" role="group" aria-label="Mockup slide">
  <use href="#chrome"/>
  <text x="16" y="19" class="h">MOCKUP SLIDE</text>
  <rect x="0" y="30" width="150" height="130" fill="#f1f2f2"/>
  <rect x="15" y="52" width="118" height="80" fill="url(#photo-office)" role="img" aria-label="Laptop showing data dashboard photo"/>
  <use href="#copy-long" x="160" y="33"/>
  <circle cx="170" cy="76" r="6" fill="#0d0d0d"/><text x="170" y="78" font-size="4.5" text-anchor="middle" class="wt">01</text>
  <circle cx="240" cy="76" r="6" fill="#237a7c"/><text x="240" y="78" font-size="4.5" text-anchor="middle" class="wt">02</text>
  <text x="164" y="92" font-size="3.8" class="bk">Your Title Here</text><text x="234" y="92" font-size="3.8" class="tl">Your Title Here</text>
  <use href="#copy-three" x="164" y="98"/><use href="#copy-three" x="234" y="98"/>
</svg>

<svg class="slide thumb" style="left:194px;top:1095px" viewBox="0 0 310 174" role="group" aria-label="Organisation chart slide">
  <use href="#chrome"/>
  <text x="16" y="19" class="h">TITLE GOES HERE</text>
  <g fill="none" stroke="#555" stroke-width=".6">
    <line x1="133" y1="40" x2="133" y2="50"/><line x1="42" y1="50" x2="224" y2="50"/>
    <line x1="42" y1="50" x2="42" y2="58"/><line x1="88" y1="50" x2="88" y2="58"/><line x1="133" y1="50" x2="133" y2="58"/><line x1="179" y1="50" x2="179" y2="58"/><line x1="224" y1="50" x2="224" y2="58"/>
    <rect x="22" y="88" width="40" height="60"/><rect x="68" y="88" width="40" height="60"/><rect x="113" y="88" width="40" height="60"/><rect x="159" y="88" width="40" height="60"/><rect x="204" y="88" width="40" height="60"/>
  </g>
  <g fill="#2f5e6b"><circle cx="133" cy="33" r="4"/><circle cx="42" cy="64" r="3.5"/><circle cx="88" cy="64" r="3.5"/><circle cx="133" cy="64" r="3.5"/><circle cx="179" cy="64" r="3.5"/><circle cx="224" cy="64" r="3.5"/><circle cx="276" cy="78" r="4"/></g>
  <g fill="#0d0d0d"><rect x="24" y="72" width="36" height="8"/><rect x="70" y="72" width="36" height="8"/><rect x="115" y="72" width="36" height="8"/><rect x="161" y="72" width="36" height="8"/><rect x="206" y="72" width="36" height="8"/></g>
  <g font-size="3.4" text-anchor="middle" class="wt" font-weight="600"><text x="42" y="77.5">YOUR TEXT</text><text x="88" y="77.5">YOUR TEXT</text><text x="133" y="77.5">YOUR TEXT</text><text x="179" y="77.5">YOUR TEXT</text><text x="224" y="77.5">YOUR TEXT</text></g>
  <g fill="#fff" stroke="#bbb" stroke-width=".5"><rect x="26" y="92" width="32" height="10"/><rect x="72" y="92" width="32" height="10"/><rect x="117" y="92" width="32" height="10"/><rect x="163" y="92" width="32" height="10"/><rect x="208" y="92" width="32" height="10"/>
  <rect x="72" y="110" width="32" height="10"/><rect x="117" y="110" width="32" height="10"/><rect x="163" y="110" width="32" height="10"/><rect x="208" y="110" width="32" height="10"/>
  <rect x="117" y="128" width="32" height="10"/><rect x="163" y="128" width="32" height="10"/><rect x="208" y="128" width="32" height="10"/></g>
  <g font-size="2.8" fill="#6f7578" text-anchor="middle">
    <text x="42" y="98">Lorem ipsum</text><text x="88" y="98">Lorem ipsum</text><text x="133" y="98">Lorem ipsum</text><text x="179" y="98">Lorem ipsum</text><text x="224" y="98">Lorem ipsum</text>
    <text x="88" y="116">Lorem ipsum</text><text x="133" y="116">Lorem ipsum</text><text x="179" y="116">Lorem ipsum</text><text x="224" y="116">Lorem ipsum</text>
    <text x="133" y="134">Lorem ipsum</text><text x="179" y="134">Lorem ipsum</text><text x="224" y="134">Lorem ipsum</text>
  </g>
  <use href="#copy-narrow" x="256" y="92"/>
</svg>

<svg class="slide thumb" style="left:360px;top:1095px" viewBox="0 0 310 174" role="group" aria-label="Contact us slide">
  <use href="#chrome"/>
  <text x="16" y="19" class="h">CONTACT US</text>
  <rect x="0" y="28" width="150" height="55" fill="url(#photo-office)" role="img" aria-label="Hand touching contact icons photo"/>
  <polygon points="145,28 310,28 310,83 130,83" fill="#0d0d0d"/>
  <use href="#copy-mid" x="155" y="50" style="--copy:#e6e6e6"/>
  <g fill="#fff" stroke="#e2e4e4" stroke-width=".8"><rect x="14" y="98" width="88" height="52"/><rect x="112" y="98" width="88" height="52"/><rect x="210" y="98" width="88" height="52"/></g>
  <g font-size="4" class="bk"><text x="20" y="110">Location</text><text x="118" y="110">Contact</text><text x="216" y="110">Email</text></g>
  <g fill="none" stroke="#333" stroke-width=".7"><circle cx="92" cy="108" r="2.2"/><rect x="190" y="106" width="4" height="4"/><rect x="288" y="106" width="5" height="4"/></g>
  <g fill="#ddd"><rect x="20" y="115" width="76" height=".6"/><rect x="118" y="115" width="76" height=".6"/><rect x="216" y="115" width="76" height=".6"/></g>
  <g font-size="3.2" fill="#666">
    <text x="20" y="126">Lorem ipsum dolor sit amet,</text><text x="20" y="131">consectetuer adipiscing elit.</text>
    <text x="118" y="126">Phone : +0123 456 789</text><text x="118" y="131">Phone : +0123 456 780</text>
    <text x="216" y="126">E-mail : mail@lumeramail.com</text><text x="216" y="131">E-mail : mail@lumeramail.com</text>
  </g>
</svg>

</body>
</html>
```